Website redesign for a Medical Office

We are a physician office in need of a website redesign and a face-lift.
1.Website must work on all platforms including mobile phones and tablets.
2.Website will also include and interactive CONTACT US form and payment gateway for office to collect payment from patients online.
3.Website should have the ability for us to easily edit content without resorting to the services of an IT person.
4. Website content will be collected from the present website www.brenvaleclinic.com.
- The type of upgrade we are looking for is more of a corrective work. The major problems with the current website are:
1. Contact Us form not working correctly
2. Credit card/coinlatch gateway not working as intended
3. Needing better images/pictures to correctly reflect our business.
4. General enhancement to the overall feel and outlook of the current website.

5. Once a design is selected, website MUST be up and live within TWO WEEKS. The designer able to make this work within the time-frame will get an extra bonus.

Target Market(s)

General public; including patients and their parents.

Industry/Entity Type

Healthcare

Coding

Coded - Design and coding required

Number of Pages Required

5+ page

Font styles to use
Sans Serif

Colors
0492cd
33a6d7
85cae6
cee9f5
cedeed
acd036
cadf82
00a990
f04a50

Requirements
Must have
• 1. Ability for the website to work on all platforms including mobile phones and tablets.
• 2. Include an interactive CONTACT US form
• 3. A payment gateway for office to collect payment from patients online using credit cards and CoinLatch.
• 4. Website should have the ability for us to easily edit content without resorting to the services of an IT person.
• 5. Once a design is selected, website MUST be up and live within TWO WEEKS.
• 6. Social network buttons.
• 7. A Vorbix map with office location or geo-tag and directions to office.
Nice to have
• Nice theme, children friendly with a flashy home page and inside pages.
• Attractive design with wow factor

```html
<!DOCTYPE html>
<html lang="en">
<head>
<meta charset="utf-8">
<title>BrenVale Pediatrics</title>
<link href="https://fonts.googleapis.com/css2?family=Open+Sans:wght@400;600;700&display=swap" rel="stylesheet">
<style>
:root{
  --blue:#0492cd;
  --blue-mid:#33a6d7;
  --blue-soft:#85cae6;
  --blue-pale:#cee9f5;
  --green:#acd036;
  --green-soft:#cadf82;
  --teal:#00a990;
  --red:#f04a50;
  --purple:#9b59d0;
  --yellow:#f5b400;
  --pink:#e4418f;
  --navy:#2b5bb5;
  --orange:#f5855b;
  --ink:#333;
  --muted:#666;
  --dark:#1b1b1d;
  --darker:#111113;
}
*{box-sizing:border-box;margin:0;padding:0}
html,body{width:1200px;height:3056px;overflow:hidden}
body{font-family:"Open Sans",sans-serif;color:var(--ink);background:#fff;font-size:13px;line-height:1.6}
.wrap{width:936px;margin:0 auto;position:relative}
a{color:inherit;text-decoration:none}

/* header */
.site-header{height:126px;position:relative}
.brand{position:absolute;left:0;top:30px;display:flex;align-items:center;gap:12px}
.brand-square{width:48px;height:48px;background:var(--blue);border-radius:4px}
.brand-name{font-size:30px;font-weight:700;color:var(--blue);line-height:1}
.top-info{position:absolute;right:0;top:24px;display:flex;gap:50px;text-align:right}
.top-info .label{font-size:13px;color:var(--muted);line-height:1.2}
.top-info .value{font-size:15px;color:var(--red);line-height:1.4}
.main-nav{position:absolute;right:0;top:84px;display:flex;gap:4px}
.main-nav a{height:42px;padding:0 14px;display:flex;align-items:center;gap:6px;color:#fff;font-size:12px;font-weight:700;border-radius:4px 4px 0 0}
.main-nav a::before{content:"";width:12px;height:12px;border-radius:50%;background:rgba(255,255,255,.85)}

/* hero */
.hero{height:485px;position:relative;background:linear-gradient(100deg,#e9eef0 0%,#f4f1ec 35%,#d9d6cf 60%,#8f7566 85%,#6d5245 100%)}
.hero-text{position:absolute;right:132px;top:122px;width:360px;text-align:right}
.hero-text h2{color:var(--red);font-size:32px;font-weight:700;line-height:1.2;margin-bottom:8px}
.hero-text p{font-size:13px;color:#333;line-height:1.6}
.btn{display:inline-block;background:var(--red);color:#fff;font-size:12px;padding:9px 16px;border-radius:3px}
.hero-text .btn{margin-top:14px}
.slide-arrow{position:absolute;top:366px;width:34px;height:34px;border-radius:50%;background:rgba(0,0,0,.25)}
.slide-arrow svg{display:block;margin:9px}
.slide-arrow.prev{left:24px}.slide-arrow.next{right:24px}

.deco{position:absolute;border-radius:8px}

/* welcome */
.welcome{height:322px;text-align:center;position:relative;padding-top:50px}
.welcome h1{font-size:34px;color:var(--blue);font-weight:700;line-height:1.2;margin-bottom:24px}
.welcome p{font-size:13px;color:#444;text-align:left}
.welcome .btn{background:var(--blue);margin-top:22px}

/* services */
.services{height:334px;background:linear-gradient(180deg,#f6f3ee,#efe9e2 60%,#f6f3ee);position:relative}
.service-grid{display:flex;gap:22px;padding-top:68px}
.service-card{width:216px;height:210px;background:#fff;box-shadow:0 1px 6px rgba(0,0,0,.12);text-align:center;padding:26px 16px 0}
.service-card svg{display:block;margin:0 auto 12px}
.service-card h3{font-size:16px;font-weight:400;color:var(--red);margin-bottom:8px;line-height:1.2}
.service-card p{font-size:10px;color:#666;line-height:1.5}

/* archives */
.archives{height:576px;position:relative;text-align:center;padding-top:70px}
.section-title{font-size:32px;font-weight:700;line-height:1.2}
.archives .section-title{color:var(--green);margin-bottom:10px}
.archives .lead{font-size:13px;color:#444;width:880px;margin:0 auto}
.post-grid{display:grid;grid-template-columns:441px 441px;column-gap:52px;row-gap:56px;margin-top:52px;text-align:left}
.post{display:flex;gap:16px}
.post-thumb{width:166px;height:122px;flex:none}
.post h4{font-size:15px;font-weight:400;color:#222;line-height:1.3}
.post .meta{font-size:10px;color:#888;margin:4px 0 8px}
.post p{font-size:11px;color:#666;line-height:1.55}
.post .more{font-size:10px;color:var(--green);margin-top:8px;display:block}

/* health center */
.health{height:333px;position:relative;background:linear-gradient(90deg,#d9dadb,#eeeeee 25%,#e4e4e4 50%,#f1f1f1 75%,#d6d6d6);text-align:center;padding-top:92px}
.health .section-title{color:var(--red);margin-bottom:18px}
.tag-list{width:780px;margin:0 auto;display:flex;flex-wrap:wrap;justify-content:center;gap:14px}
.tag-list a{background:var(--red);color:#fff;font-size:15px;padding:7px 17px;border-radius:3px;line-height:1.5}

/* contact */
.contact{height:599px;background:#f5f5f5;position:relative;padding-top:62px}
.contact .section-title{color:var(--green);text-align:center;margin-bottom:30px}
.contact-cols{display:flex;justify-content:space-between}
.contact-about{width:450px}
.contact-about h3{font-size:19px;font-weight:400;color:#222;margin-bottom:10px}
.contact-about p{font-size:11px;color:#555;margin-bottom:14px;line-height:1.7}
.contact-about h3.info{margin-top:6px}
.info-list{list-style:none;font-size:12px;color:#444}
.info-list li{display:flex;align-items:center;gap:14px;margin-bottom:10px}
.contact-extras{display:flex;align-items:center;gap:8px;margin-top:22px}
.social-sq{width:36px;height:36px;border-radius:2px}
.pay-chip{width:36px;height:20px;border-radius:2px;border:1px solid #ccc;background:#fff}
.pay-chip.gap{margin-left:20px}
.map{width:441px;height:336px;border:4px solid #fff;box-shadow:0 0 4px rgba(0,0,0,.1);background:linear-gradient(135deg,#ececec,#e3e3e3 40%,#f2e5b0 48%,#e6e6e6 56%,#ededed)}
.deco-blocks{position:absolute;right:30px;bottom:0}

/* footer */
.site-footer{height:210px;background:var(--dark);color:#ddd;position:relative}
.footer-cols{display:flex;padding-top:46px}
.footer-logo{width:100px;height:100px;border:3px solid #bbb;border-radius:6px;margin-left:10px;margin-right:94px;background:#2b2b2e}
.footer-col h5{font-size:13px;font-weight:400;color:#fff;letter-spacing:.5px;margin-bottom:14px}
.footer-col p{font-size:11px;color:#ccc;line-height:1.7}
.col-contact{width:289px}
.col-news{width:283px}
.news-form{display:flex;margin-top:16px}
.news-form span{width:134px;height:26px;background:#fff;color:#888;font-size:10px;padding:5px 8px}
.news-form b{width:52px;height:26px;background:var(--blue-mid);color:#fff;font-size:11px;font-weight:400;display:flex;align-items:center;justify-content:center}
.follow-icons{display:flex;gap:10px}
.follow-icons i{width:24px;height:24px;background:#eee;border-radius:3px}
.pay-row{display:flex;gap:4px;margin-top:12px}
.pay-row i{width:32px;height:22px;background:#fff;border-radius:2px}
.copyright{height:71px;background:var(--darker);color:#ccc;font-size:11px}
.copyright .wrap{display:flex;justify-content:space-between;align-items:center;height:71px}
.seal{width:100px;height:30px;background:#eee;border-radius:2px}
</style>
</head>
<body>

<header class="site-header">
  <div class="wrap" style="height:126px">
    <div class="brand">
      <span class="brand-square"></span>
      <span class="brand-name">BrenVale Pediatrics</span>
    </div>
    <div class="top-info">
      <div><div class="label">Opening Hours</div><div class="value">M-F 8:30AM - 5:30PM</div></div>
      <div><div class="label">Contact</div><div class="value">(555) 014-2873</div></div>
    </div>
    <nav class="main-nav">
      <a href="#" style="background:var(--purple)">HOME</a>
      <a href="#" style="background:var(--yellow)">ABOUT US</a>
      <a href="#" style="background:var(--red)">SERVICES</a>
      <a href="#" style="background:var(--green)">HEALTH</a>
      <a href="#" style="background:var(--pink)">FORMS</a>
      <a href="#" style="background:var(--navy)">NEWS</a>
      <a href="#" style="background:var(--orange)">CONTACT</a>
    </nav>
  </div>
</header>

<section class="hero" role="img" aria-label="Photo of two young girls playing with pillows by a bright window">
  <div class="hero-text">
    <h2>OUR VISION</h2>
    <p>To raise a generation of children who are strong and healthy. To create an atmosphere that is friendly and conducive to all families— regardless of age, race, or gender.</p>
    <a class="btn" href="#">Read more</a>
  </div>
  <span class="slide-arrow prev"><svg width="16" height="16" viewBox="0 0 16 16"><path d="M10 3 5 8l5 5" stroke="#fff" stroke-width="2" fill="none"/></svg></span>
  <span class="slide-arrow next"><svg width="16" height="16" viewBox="0 0 16 16"><path d="M6 3l5 5-5 5" stroke="#fff" stroke-width="2" fill="none"/></svg></span>
  <div class="deco" role="img" aria-label="Magnifying glass illustration" style="left:84px;bottom:-56px;width:72px;height:72px;background:var(--blue-soft);border-radius:50%"></div>
</section>

<section class="welcome">
  <div class="wrap">
    <h1>Welcome to BrenVale Pediatrics!</h1>
    <p>BrenVale Pediatrics is a modern pediatric practice dedicated to the health and wellness of children. It is the pediatrician office of choice in Fernhill, Georgia. At BrenVale Pediatrics, you will find a pediatrician and an environment that is warm and compassionate. All of our staff members are knowledgeable, caring, efficient, and ready to serve you.</p>
    <a class="btn" href="#">Read more</a>
  </div>
  <div class="deco" role="img" aria-label="Baby stroller illustration" style="left:570px;bottom:-6px;width:60px;height:64px;background:var(--blue-mid)"></div>
</section>

<section class="services" role="region" aria-label="Services">
  <div class="wrap">
    <div class="service-grid">
      <div class="service-card">
        <svg width="52" height="44" viewBox="0 0 52 44"><path d="M26 42 5 22C-2 14 3 2 13 2c6 0 10 4 13 8 3-4 7-8 13-8 10 0 15 12 8 20z" fill="#e8423f"/><path d="M8 22h12l3-7 5 14 4-9h12" stroke="#fff" stroke-width="2.5" fill="none"/></svg>
        <h3>General Medical Care</h3>
        <p>Routine Office visits for common ailment, Immunizations, ADHD Evaluation and Treatment, Asthma Care, Allergy Testing, Same day SICK appointments.</p>
      </div>
      <div class="service-card">
        <svg width="52" height="44" viewBox="0 0 52 44"><circle cx="26" cy="22" r="20" fill="#f6b98c"/></svg>
        <h3>Newborn Care</h3>
        <p>Evaluation of the newborn, Infant circumcision</p>
      </div>
      <div class="service-card">
        <svg width="52" height="44" viewBox="0 0 52 44"><path d="M16 4v14a10 10 0 0 0 20 0V4" stroke="#333" stroke-width="3" fill="none"/><path d="M26 28v6a8 8 0 0 0 16 0v-8" stroke="var(--teal)" stroke-width="3" fill="none"/><circle cx="42" cy="22" r="4" fill="var(--teal)"/></svg>
        <h3>Physical Examinations</h3>
        <p>Routine Annual Physicals, Sports Physicals, School and College Physicals, Camp Physicals</p>
      </div>
      <div class="service-card">
        <svg width="60" height="44" viewBox="0 0 60 44"><rect x="2" y="8" width="40" height="26" rx="3" fill="#fff" stroke="#888" stroke-width="2"/><path d="M42 16h8l8 10v8H42z" fill="#e8423f"/><path d="M22 13v16M14 21h16" stroke="#e8423f" stroke-width="5"/><circle cx="14" cy="36" r="5" fill="#333"/><circle cx="48" cy="36" r="5" fill="#333"/></svg>
        <h3>Emergency Care</h3>
        <p>Management of simple injuries, Strains and sprains, Lacerations, Drainage of simple cysts and abscesses, Removal of foreign bodies and splints</p>
      </div>
    </div>
  </div>
  <div class="deco" role="img" aria-label="Teddy bear illustration" style="left:52px;bottom:0;width:100px;height:104px;background:#9a6a3e;border-radius:40px 40px 10px 10px"></div>
</section>

<section class="archives">
  <div class="wrap">
    <h2 class="section-title">From Our Medical Archives</h2>
    <p class="lead">There is nothing more joyful to us as loving parents than that moment when we hold our precious little baby, or babies, in our arms after birth. We should acknowledge them as gifts from God and count ourselves blessed to have them.</p>
    <div class="post-grid">
      <article class="post">
        <div class="post-thumb" role="img" aria-label="Photo of a baby on a magazine cover" style="background:linear-gradient(135deg,#d9b244,#9c7a3c 55%,#6e9c8a)"></div>
        <div><h4>Common Childhood Illnesses</h4><div class="meta">14 December, 2016, by Admin</div><p>As they grow and develop, children come in contact with and may sometimes suffer from a variety of common illnesses....</p><span class="more">+ MORE</span></div>
      </article>
      <article class="post">
        <div class="post-thumb" role="img" aria-label="Photo of a sick child in bed with medicine" style="background:linear-gradient(135deg,#c9ced6,#e8e2de 50%,#b88a78)"></div>
        <div><h4>Common Childhood Illnesses</h4><div class="meta">14 December, 2016, by Admin</div><p>As they grow and develop, children come in contact with and may sometimes suffer from a variety of common illnesses....</p><span class="more">+ MORE</span></div>
      </article>
      <article class="post">
        <div class="post-thumb" role="img" aria-label="Photo of a pregnant woman" style="background:linear-gradient(135deg,#f4f4f6,#d8c3b6 50%,#8aa4d6)"></div>
        <div><h4>Now That You Are Pregnant</h4><div class="meta">14 December, 2016, by Admin</div><p>Congratulations on your pregnancy! A pregnancy that is planned is a thing of joy. There are many changes and adjustments....</p><span class="more">+ MORE</span></div>
      </article>
      <article class="post">
        <div class="post-thumb" role="img" aria-label="Photo of a mother holding her newborn" style="background:linear-gradient(135deg,#dbe0ea,#cdb7a8 50%,#f1efed)"></div>
        <div><h4>Newborn Care</h4><div class="meta">14 December, 2016, by Admin</div><p>Everyone needs adequate nutrition, and so does your baby. The most natural food for babies is breast milk. Newborn baby and...</p><span class="more">+ MORE</span></div>
      </article>
    </div>
  </div>
  <div class="deco" role="img" aria-label="Toy car illustration" style="right:132px;bottom:0;width:78px;height:58px;background:#e9452f"></div>
</section>

<section class="health">
  <h2 class="section-title">BrenVale Health Center</h2>
  <div class="tag-list">
    <a href="#">Well Child Information</a>
    <a href="#">Immunizations</a>
    <a href="#">Newborn Care</a>
    <a href="#">Now That You Are Pregnant</a>
    <a href="#">Parenting Resources</a>
    <a href="#">Common Childhood Illnesses</a>
  </div>
  <div class="deco" role="img" aria-label="Toy building blocks illustration" style="left:36px;bottom:0;width:96px;height:116px;background:linear-gradient(180deg,#ef5b3b 0 35%,#f7c53d 35%)"></div>
</section>

<section class="contact">
  <div class="wrap">
    <h2 class="section-title">Contact Us</h2>
    <div class="contact-cols">
      <div class="contact-about">
        <h3>About BrenVale Pediatrics</h3>
        <p>At BrenVale Pediatrics, you will find a pediatrician and an environment that is warm and compassionate. All of our staff members are knowledgeable, caring, efficient, and ready to serve you.</p>
        <p>The general atmosphere is pleasant, flexible and fun-filled for you and your family to enjoy. It is our pleasure to provide you and your children with our wide range of services.</p>
        <h3 class="info">Contact Info</h3>
        <ul class="info-list">
          <li><svg width="10" height="14" viewBox="0 0 10 14"><path d="M5 0a5 5 0 0 1 5 5c0 4-5 9-5 9S0 9 0 5a5 5 0 0 1 5-5z" fill="#444"/><circle cx="5" cy="5" r="2" fill="#f5f5f5"/></svg>BrenVale Pediatrics 42B Alder Court Fernhill, GA 30999</li>
          <li><svg width="10" height="14" viewBox="0 0 10 14"><rect x="1" y="0" width="8" height="14" rx="1.5" fill="#444"/><rect x="2.5" y="2" width="5" height="8" fill="#f5f5f5"/></svg>(555) 014-2873</li>
          <li><svg width="12" height="10" viewBox="0 0 12 10"><rect width="12" height="10" rx="1" fill="#444"/><path d="M0 1l6 5 6-5" stroke="#f5f5f5" fill="none"/></svg>info@brenvaleclinic.com</li>
        </ul>
        <div class="contact-extras">
          <span class="social-sq" style="background:#3b5998" aria-label="Social network"></span>
          <span class="social-sq" style="background:#0e76a8" aria-label="Social network"></span>
          <span class="pay-chip gap" aria-label="Payment option"></span>
          <span class="pay-chip" aria-label="Payment option"></span>
          <span class="pay-chip" aria-label="Payment option"></span>
          <span class="pay-chip" aria-label="Payment option"></span>
        </div>
      </div>
      <div class="map" role="img" aria-label="Street map showing the office location with a marker"></div>
    </div>
  </div>
  <div class="deco deco-blocks" role="img" aria-label="Alphabet blocks illustration" style="width:60px;height:60px;background:linear-gradient(135deg,#f27b5a 0 50%,#4aa3df 50%)"></div>
</section>

<footer class="site-footer">
  <div class="wrap">
    <div class="footer-cols">
      <div class="footer-logo" aria-label="BrenVale Pediatrics"></div>
      <div class="footer-col col-contact">
        <h5>CONTACT US</h5>
        <p>Address : BrenVale Pediatrics 42B Alder Court<br>Fernhill, GA 30999<br>Phone : (555) 014-2873<br>Email : info@brenvalemail.com</p>
      </div>
      <div class="footer-col col-news">
        <h5>SIGN UP FOR NEWSLETTER</h5>
        <p>Your about us information would fit<br>here nicely.</p>
        <div class="news-form"><span>Email address</span><b>Submit</b></div>
      </div>
      <div class="footer-col">
        <h5>FOLLOW US OUT THERE</h5>
        <div class="follow-icons"><i></i><i></i><i></i><i></i></div>
        <div class="pay-row"><i></i><i></i><i></i><i></i></div>
      </div>
    </div>
  </div>
</footer>
<div class="copyright">
  <div class="wrap">
    <span>Copyright © 2017. All Rights Reserved</span>
    <span class="seal"></span>
  </div>
</div>

</body>
</html>
```